Design of a can of the adaptogenic drink brand "Brivana" (vector)

Please take the cans from the brief and make a print-ready vector with the instructions as in the other photos.

Target Market(s)

Young, upper-middle class athlete

Industry/Entity Type

Agroalimentaire

Colors

Designer to choose colors to be used in the design.

Requirements
Must have
• Adaptogenic flawed water
Nice to have
• Sleek, classy and healthy

```html
<!DOCTYPE html>
<html lang="en">
<head>
<meta charset="utf-8">
<title>Brivana – can design</title>
<link href="https://fonts.googleapis.com/css2?family=Montserrat:wght@500;700;800&display=swap" rel="stylesheet">
<style>
  :root{
    --purple:#3a2c91;
    --purple-light:#c9c1ee;
    --sky:#3aa6d6;
    --sky-light:#d8eef8;
    --night:#24203f;
    --night-mid:#4a3f7e;
    --teal:#1c3744;
    --teal-mid:#3f7b8e;
    --ink:#111114;
    --grey:#8a8a8f;
    --white:#ffffff;
    --paper:#ffffff;
  }
  *{margin:0;padding:0;box-sizing:border-box}
  html,body{width:677px;height:1200px;overflow:hidden;background:var(--paper)}
  body{position:relative;font-family:"Montserrat",Arial,sans-serif}

  .labels{position:absolute;top:38px;left:61px;width:579px;height:255px;display:flex;justify-content:space-between}
  .label{width:120px;height:255px;position:relative;display:flex;flex-direction:column;align-items:center;color:var(--white)}
  .label--purple{background:linear-gradient(180deg,var(--purple-light) 0%,#f2f0fb 35%,#d7d1f3 60%,var(--purple) 100%);color:var(--purple)}
  .label--sky{background:linear-gradient(180deg,var(--sky-light) 0%,#f4fafd 35%,#bfe2f3 60%,var(--sky) 100%);color:var(--sky)}
  .label--night{background:linear-gradient(180deg,var(--night) 0%,#302a55 50%,var(--night-mid) 100%)}
  .label--teal{background:linear-gradient(180deg,var(--teal) 0%,#244554 50%,var(--teal-mid) 100%)}
  .label__name{margin-top:58px;font-weight:800;font-size:20px;letter-spacing:-0.5px}
  .label__tier{font-weight:700;font-size:7px;letter-spacing:2px;margin-top:2px}
  .label__molecule{width:80px;height:56px;margin-top:28px;border-radius:6px;background:radial-gradient(circle,rgba(255,255,255,.55),rgba(255,255,255,0) 70%)}
  .label__volume{position:absolute;bottom:16px;font-size:6px;font-weight:500}
  .label--purple .label__volume,.label--sky .label__volume{color:var(--white)}

  .wordmarks{position:absolute;top:312px;left:60px;width:560px;display:flex;justify-content:space-between}
  .wordmark{font-weight:800;font-size:36px;letter-spacing:-1px;line-height:1}
  .wordmark--purple{color:var(--purple)}
  .wordmark--grey{color:var(--grey)}

  .band{position:absolute;top:372px;height:70px;display:flex;align-items:center;justify-content:center}
  .band--purple{left:0;width:338px;background:var(--purple)}
  .band--black{left:338px;width:339px;height:290px;background:var(--ink);align-items:flex-start;padding-top:18px}
  .band .wordmark{font-size:34px}
  .band--purple .wordmark{color:var(--white)}
  .band--black .wordmark{color:var(--grey)}

  .hero{position:absolute;top:460px;height:190px;width:338px;display:flex;align-items:center;justify-content:center}
  .hero--light{left:0}
  .hero--dark{left:338px}
  .hero .wordmark{font-size:62px;letter-spacing:-2px}
  .hero--light .wordmark{color:var(--purple)}
  .hero--dark .wordmark{color:var(--white)}

  .cans{position:absolute;top:700px;left:32px;width:613px;height:480px;display:flex;justify-content:space-between}
  .can{width:142px;height:480px;border-radius:14px 14px 10px 10px;position:relative;display:flex;flex-direction:column;align-items:center;overflow:hidden}
  .can::before{content:"";position:absolute;top:0;left:0;right:0;height:18px;background:linear-gradient(90deg,#9a9aa3,#e9e9ee 45%,#8c8c95)}
  .can::after{content:"";position:absolute;bottom:0;left:0;right:0;height:10px;background:linear-gradient(90deg,#8c8c95,#dcdce2 45%,#8c8c95)}
  .can .label__name{margin-top:120px;font-size:26px}
  .can .label__tier{font-size:9px}
  .can .label__molecule{width:100px;height:70px;margin-top:40px}
  .can .label__volume{bottom:24px;font-size:8px}
</style>
</head>
<body>

  <section class="labels">
    <div class="label label--purple">
      <span class="label__name">Brivana</span><span class="label__tier">PREMIUM</span>
      <div class="label__molecule" role="img" aria-label="Water molecule diagram"></div>
      <span class="label__volume">8.5oz / 250ml</span>
    </div>
    <div class="label label--sky">
      <span class="label__name">Brivana</span><span class="label__tier">PREMIUM</span>
      <div class="label__molecule" role="img" aria-label="Water molecule diagram"></div>
      <span class="label__volume">8.5oz / 250ml</span>
    </div>
    <div class="label label--night">
      <span class="label__name">Brivana</span><span class="label__tier">PREMIUM</span>
      <div class="label__molecule" role="img" aria-label="Water molecule diagram"></div>
      <span class="label__volume">8.5oz / 250ml</span>
    </div>
    <div class="label label--teal">
      <span class="label__name">Brivana</span><span class="label__tier">PREMIUM</span>
      <div class="label__molecule" role="img" aria-label="Water molecule diagram"></div>
      <span class="label__volume">8.5oz / 250ml</span>
    </div>
  </section>

  <section class="wordmarks">
    <span class="wordmark wordmark--purple">Brivana</span>
    <span class="wordmark wordmark--grey">Brivana</span>
  </section>

  <div class="band band--purple"><span class="wordmark">Brivana</span></div>
  <div class="band band--black"><span class="wordmark">Brivana</span></div>

  <div class="hero hero--light"><span class="wordmark">Brivana</span></div>
  <div class="hero hero--dark"><span class="wordmark">Brivana</span></div>

  <section class="cans">
    <div class="can label--sky">
      <span class="label__name">Brivana</span><span class="label__tier">PREMIUM</span>
      <div class="label__molecule" role="img" aria-label="Water molecule diagram"></div>
      <span class="label__volume">8.5oz / 250ml</span>
    </div>
    <div class="can label--purple">
      <span class="label__name">Brivana</span><span class="label__tier">PREMIUM</span>
      <div class="label__molecule" role="img" aria-label="Water molecule diagram"></div>
      <span class="label__volume">8.5oz / 250ml</span>
    </div>
    <div class="can label--night">
      <span class="label__name">Brivana</span><span class="label__tier">PREMIUM</span>
      <div class="label__molecule" role="img" aria-label="Water molecule diagram"></div>
      <span class="label__volume">8.5oz / 250ml</span>
    </div>
    <div class="can label--teal">
      <span class="label__name">Brivana</span><span class="label__tier">PREMIUM</span>
      <div class="label__molecule" role="img" aria-label="Water molecule diagram"></div>
      <span class="label__volume">8.5oz / 250ml</span>
    </div>
  </section>

</body>
</html>
```